Update the A4 Specials Page for Restaurant/Cafe

Provide a MINIMALIST attractive Specials page we can print weekly for our food and drink specials to give to our guests. Final design is to be provided in WORD Document so it can be easily edited by Manager. Should be black text and MINIMALIST to minimise ink usage as we print hundreds a week. We have UPLOADED the existing page as a template for you to update. Maybe logo can stay, see what you think. Or delete it and do something else. Keep it simple. Choose a good FONT. Could be a little playful with a cocktail ICON or something. Our existing menus can be seen at www.tallowmillcafe.com.au and they are using font Alegreya. Please note we are unable to provide any feedback to designers, however we really do appreciate your time if you are submitting a design. Thank you for your participation.

```html
<!DOCTYPE html>
<html lang="en">
<head>
<meta charset="utf-8">
<title>Tallow Mill Cafe – Weekly Specials</title>
<link rel="stylesheet" href="https://fonts.googleapis.com/css2?family=Alegreya:ital,wght@0,400;0,700;0,800;0,900;1,400&display=swap">
<style>
  :root {
    --backdrop: #e6e4e0;
    --paper: #f3f3f2;
    --ink: #2b2b2b;
    --ink-soft: #3a3a3a;
    --ribbon-text: #f3f3f2;
    --art-tone: #c9c9c7;
    --art-tone-light: #e2e2e0;
  }
  * { box-sizing: border-box; margin: 0; padding: 0; }
  html, body {
    width: 1200px;
    height: 1106px;
    overflow: hidden;
    background: var(--backdrop);
  }
  body {
    font-family: "Alegreya", Georgia, serif;
    color: var(--ink);
    display: flex;
    align-items: center;
    justify-content: center;
  }
  .specials-page {
    position: relative;
    width: 764px;
    height: 1080px;
    background: var(--paper);
    box-shadow: 0 2px 10px rgba(0,0,0,0.12);
  }
  .page-frame {
    position: absolute;
    inset: 24px;
    border: 2px dashed var(--ink);
  }
  .page-content {
    position: absolute;
    inset: 24px;
    padding: 26px 70px 0;
    display: flex;
    flex-direction: column;
    align-items: center;
  }

  /* Masthead */
  .masthead {
    width: 100%;
    height: 170px;
    position: relative;
    display: flex;
    justify-content: center;
    align-items: center;
  }
  .artwork {
    position: absolute;
    top: 10px;
    width: 140px;
    height: 150px;
    border-radius: 6px;
    background: radial-gradient(circle at 50% 55%, var(--art-tone) 0%, var(--art-tone-light) 70%, transparent 100%);
  }
  .artwork--grapes { left: -20px; top: 60px; }
  .artwork--cocktail { right: -20px; top: 0; }
  .brand-name {
    font-weight: 900;
    font-size: 52px;
    line-height: 0.95;
    text-align: center;
    letter-spacing: 0.5px;
    text-transform: uppercase;
    color: var(--ink);
    margin-top: 20px;
  }

  /* Sections */
  .section-title {
    font-weight: 800;
    font-size: 44px;
    line-height: 1;
    text-transform: uppercase;
    text-align: center;
    letter-spacing: 0.3px;
  }
  .section-title--spaced { margin-top: 44px; }
  .section-title--first { margin-top: 36px; }

  .ribbon {
    margin-top: 14px;
    height: 36px;
    padding: 0 48px;
    background: var(--ink);
    color: var(--ribbon-text);
    font-weight: 800;
    font-size: 14px;
    letter-spacing: 1px;
    text-transform: uppercase;
    display: flex;
    align-items: center;
    justify-content: center;
    clip-path: polygon(0 0, 100% 0, 92% 50%, 100% 100%, 0 100%, 8% 50%);
  }

  .menu-item {
    width: 100%;
    display: flex;
    align-items: flex-end;
    margin-top: 14px;
  }
  .menu-item--solo { margin-top: 62px; }
  .item-description {
    font-size: 16px;
    line-height: 1.35;
    color: var(--ink-soft);
    white-space: nowrap;
  }
  .item-leader {
    flex: 1;
    border-bottom: 1.5px dashed var(--ink);
    margin: 0 6px 6px;
    min-width: 40px;
  }
  .item-price {
    font-weight: 800;
    font-size: 24px;
    line-height: 1;
    align-self: flex-start;
  }
  .item-description--caps { text-transform: uppercase; letter-spacing: 0.5px; }
</style>
</head>
<body>
  <main class="specials-page">
    <div class="page-frame"></div>
    <div class="page-content">

      <header class="masthead">
        <div class="artwork artwork--grapes" role="img" aria-label="Engraved illustration of a bunch of grapes with vine leaves"></div>
        <h1 class="brand-name">Tallow Mill<br>Cafe</h1>
        <div class="artwork artwork--cocktail" role="img" aria-label="Line drawing of a cocktail glass with ice, citrus slices and mint"></div>
      </header>

      <h2 class="section-title section-title--first">Weekly Specials</h2>

      <div class="ribbon">Chicken Filo</div>
      <div class="menu-item">
        <p class="item-description">Creamy Chicken with Pinenuts, wrapped in Filo Pastry.<br>Served with Side Salad &amp; Zulu Sauce</p>
        <span class="item-leader"></span>
        <span class="item-price">$24</span>
      </div>

      <div class="ribbon">Minestrone Soup</div>
      <div class="menu-item">
        <p class="item-description">Served with Garlic Bread</p>
        <span class="item-leader"></span>
        <span class="item-price">$08</span>
      </div>

      <h2 class="section-title section-title--spaced">Cocktail Special</h2>

      <div class="ribbon">Passionista</div>
      <div class="menu-item">
        <p class="item-description">Vodka, Passionfruit Pulp, Mango Puree<br>Top up with Ginger &amp; Lemon Kombucha</p>
        <span class="item-leader"></span>
        <span class="item-price">$17</span>
      </div>

      <h2 class="section-title section-title--spaced">Craft<br>Beer Special</h2>

      <div class="menu-item menu-item--solo">
        <p class="item-description"><span class="item-description--caps">Quiet Gecko</span><br><span class="item-description--caps">Mango Burst</span><br>Tropical Pale Ale 4.8% Alc.</p>
        <span class="item-leader"></span>
        <span class="item-price">$10</span>
      </div>

    </div>
  </main>
</body>
</html>
```